Zielgruppe
Wohnungsbaugenossenschaft, Vermietung von Wohnungen
Mieter
Aufgabenstellung
Logo , siehe upload
- Standorte mit freien Wohnungen sollen dominant platziert werden
- aktuelle Meldungen, Havarienummer ( siehe hier: https://www.wbg-kelmsried.example/)
- weitere Kommunikationsdaten gut sichtbar, auch Öffnungszeiten

```html
<!DOCTYPE html>
<html lang="de">
<head>
<meta charset="utf-8">
<title>Wohnungsbaugenossenschaft Kelmsried eG</title>
<link rel="stylesheet" href="https://fonts.googleapis.com/css2?family=Comfortaa:wght@600;700&family=Open+Sans:ital,wght@0,300;0,400;0,600;0,700;1,300&family=Oswald:wght@300;400&family=Baloo+2:wght@700&display=swap">
<style>
:root{
  --blue:#2d3e98;
  --red:#e30613;
  --side:#c4c8e6;
  --lav:#a9acd6;
  --box-dark:#535d9b;
  --box-mid:#6d77b9;
  --box-light:#aab0da;
  --grey-card:#efeff1;
  --text:#666;
  --pale:#f1f1f6;
}
*{box-sizing:border-box;margin:0;padding:0}
html,body{width:1200px;height:2508px;overflow:hidden}
body{position:relative;background:#fff;font-family:"Open Sans",sans-serif;color:var(--text);font-weight:300}
.abs{position:absolute}
.btn{position:absolute;background:var(--red);color:#fff;font-family:"Open Sans",sans-serif;font-weight:400;font-size:10.5px;text-transform:uppercase;display:flex;align-items:center;justify-content:center;white-space:nowrap}
.display{font-family:"Comfortaa",sans-serif;font-weight:700;color:var(--blue);white-space:nowrap}
.kicker{font-style:italic;font-weight:300;font-size:16px;color:#555}
.img{position:absolute}

.sidebar{left:0;top:0;width:185px;height:2508px;background:var(--side)}
.brand{left:0;top:0;width:185px;height:178px;background:#fff;display:flex;flex-direction:column;align-items:center;justify-content:center;gap:8px}
.brand .mark{display:flex;align-items:center;gap:8px;font-family:"Comfortaa",sans-serif;font-weight:700;font-size:22px;color:var(--blue);white-space:nowrap}
.brand .mark span.sq{width:14px;height:14px;background:var(--red)}
.brand .claim{font-family:"Comfortaa",sans-serif;font-weight:700;font-size:12px;color:var(--blue);text-align:center;line-height:1.3}
.nav{left:0;top:180px;width:185px}
.nav a{display:block;height:36px;line-height:36px;padding-left:24px;font-family:"Oswald",sans-serif;font-weight:300;font-size:12.5px;color:var(--blue);text-decoration:none;position:relative}
.nav a:after{content:"";position:absolute;left:18px;right:18px;bottom:0;height:1px;background:#8e94c4}
.nav a.active{background:var(--red);color:#fff;font-weight:400}
.nav a.active:after,.nav a:last-child:after{display:none}
.side-phone{left:0;top:475px;width:185px;height:31px;background:var(--blue);color:#fff;font-family:"Baloo 2",sans-serif;font-size:17px;display:flex;align-items:center;gap:8px;padding-left:22px;white-space:nowrap}

.topbar{left:185px;top:0;width:1015px;height:40px;font-size:11px;color:#777}
.topbar .contact{position:absolute;left:15px;top:13px;display:flex;gap:14px;align-items:center}
.topbar .contact span{display:flex;align-items:center;gap:5px}
.toplinks{position:absolute;right:25px;top:15px;font-family:"Oswald",sans-serif;font-size:9.5px;color:#8a8a8a;letter-spacing:.2px}
.toplinks i{font-style:normal;margin:0 6px}
.band{left:185px;top:40px;width:1015px;height:38px;background:var(--blue);color:#fff;font-family:"Baloo 2",sans-serif;font-size:18px;letter-spacing:.5px}
.band .name{position:absolute;left:18px;top:7px;text-transform:uppercase}
.band .hav{position:absolute;left:672px;top:0;width:323px;height:38px;background:#5462aa;display:flex;align-items:center;justify-content:center}

.hero{left:185px;top:78px;width:1015px;height:332px;background:linear-gradient(90deg,#caa286 0%,#e8e2da 30%,#f4f2ee 55%,#efe8dc 75%,#b99b7c 100%)}
.hero-title{left:668px;top:128px;font-family:"Comfortaa",sans-serif;font-weight:600;font-size:29px;line-height:39px;color:var(--blue);letter-spacing:.5px}
.hero-sub{left:671px;top:209px;font-size:12.5px;line-height:20px;color:#555;text-transform:uppercase;font-weight:400}

.free-panel{left:203px;top:366px;width:977px;height:80px;background:#fff}
.sec-title{width:100%;text-align:center;font-size:30px}
.free-sub{top:418px;left:185px;width:1015px;text-align:center;font-size:12px;color:#777}
.flat{position:absolute;top:454px;width:229px;height:236px;background:var(--grey-card);text-align:center;font-size:11px;line-height:16px;color:#777}
.flat .pic{height:137px}
.flat b{display:block;margin-top:9px;font-size:12px;font-weight:600;color:#555}
.flat .btn{left:50%;transform:translateX(-50%);top:201px;height:23px;padding:0 10px}

.welcome-title{font-size:30px}
.body-text{font-size:12.5px;line-height:16.5px;color:#6f6f6f}

.rbox{position:absolute;left:935px;width:245px;color:#fff}
.rbox h3{font-family:"Comfortaa",sans-serif;font-weight:600;font-size:18px;display:flex;align-items:center;gap:7px;white-space:nowrap}
.rbox .row{display:flex;align-items:center;gap:7px;font-size:9.5px;margin-top:5px;font-weight:400}
.hours{font-size:9.2px;line-height:15.5px;font-weight:400}
.hours b{font-weight:700;display:inline-block;width:22px}
.loc{position:absolute;left:954px;width:206px;height:22px;line-height:22px;padding-left:8px;font-size:12px;color:#777}
.loc.alt{background:#c8cbe6}

.news{position:absolute;top:1377px;width:222px;height:206px}
.news .pic{height:148px}
.news .card{position:absolute;left:20px;top:88px;width:180px;height:118px;background:#fff;padding:20px 0 0 22px}
.news .date{font-size:10px;color:#777;display:flex;gap:5px;align-items:center}
.news .ttl{font-family:"Open Sans",sans-serif;font-size:15px;color:var(--blue);margin-top:6px;font-weight:400}
.news .tx{font-size:9px;line-height:14px;color:#888;margin-top:4px}
.news .btn{left:42px;top:186px;height:18px;width:98px;font-size:9.5px}

.contact-sec{left:185px;top:1812px;width:1015px;height:696px;background:var(--pale)}
.field-label{font-size:12.5px;color:#666;display:flex;align-items:center;gap:6px}
.field{position:absolute;left:803px;width:370px;height:36px;background:#fff}
.caddr{display:flex;align-items:center;gap:10px;font-size:13px;color:#6f6f6f;white-space:nowrap}

.foot-head{font-family:"Comfortaa",sans-serif;font-weight:600;font-size:20px;color:#fff;letter-spacing:.3px}
.foot-head:after{content:"";display:block;width:85px;height:1px;background:#fff;margin-top:4px}
.foot-text{color:#fff;font-size:11.5px;line-height:17px;font-weight:400}
.fhours b{font-weight:700;display:inline-block;width:26px}
.fnav{font-size:11.5px;line-height:17px;color:#fff;text-transform:uppercase;font-weight:300}
</style>
</head>
<body>

<div class="abs sidebar"></div>
<div class="abs brand">
  <div class="mark"><span class="sq"></span>wbg Kelmsried</div>
  <div class="claim">Zusammen wohnen –<br>gut leben!</div>
</div>
<nav class="abs nav">
  <a class="active">HOME</a>
  <a>DIE GENOSSENSCHAFT</a>
  <a>WOHNUNGSSUCHE</a>
  <a>AKTUELLES</a>
  <a>HAVARIEDIENST</a>
  <a>KONTAKT</a>
</nav>
<div class="img" role="img" aria-label="Emblem Lebensart" style="left:32px;top:424px;width:124px;height:36px;background:#b8bce0"></div>
<div class="abs side-phone">
  <svg width="10" height="17" viewBox="0 0 10 17"><rect x="1" y="1" width="8" height="15" rx="1.5" fill="none" stroke="#fff" stroke-width="1.6"/><circle cx="5" cy="13" r="1" fill="#fff"/></svg>
  0 34 99 / 55 20 88
</div>

<div class="abs topbar">
  <div class="contact">
    <span><svg width="10" height="14" viewBox="0 0 10 14"><path d="M5 0C2.2 0 0 2.2 0 5c0 3.5 5 9 5 9s5-5.5 5-9c0-2.8-2.2-5-5-5zm0 7a2 2 0 110-4 2 2 0 010 4z" fill="var(--red)"/></svg>Lindenhofstraße 13, 07491 Kelmsried</span>
    <span><svg width="12" height="9" viewBox="0 0 12 9"><rect width="12" height="9" fill="var(--red)"/><path d="M0 0l6 5 6-5" stroke="#fff" fill="none"/></svg>kontakt@wbg-kelmsried.example</span>
  </div>
  <div class="toplinks">SERVICE<i>|</i>MIETERZEITUNG<i>|</i>PARTNER<i>|</i>DOWNLOAD<i>|</i>IMPRESSUM<i>|</i>DATENSCHUTZERKLÄRUNG</div>
</div>
<div class="abs band">
  <div class="name">Wohnungsbaugenossenschaft Kelmsried eG</div>
  <div class="hav">Havarienummer: 0176 / 555 031 70</div>
</div>

<div class="img hero" role="img" aria-label="Foto: lachende Frau mit Wohnungsschlüssel und lächelnder Mann in heller Wohnung"></div>
<div class="abs hero-title">LEBEN WO SIE SICH<br>WOHLFÜHLEN</div>
<div class="abs hero-sub">Ihr neues Zu Hause. Neue Wohnkonzepte<br>und ein angenehmes Wohnfeld. Bei uns<br>werden Sie glücklich!</div>
<div class="btn" style="left:672px;top:279px;width:180px;height:24px">Zu den Wohnungsangeboten</div>

<div class="abs free-panel"></div>
<div class="abs display sec-title" style="left:185px;width:1015px;top:377px">Freie Wohnungen</div>
<div class="abs free-sub">Informationen zu weiteren Wohnungsangeboten erhalten Sie persönlich oder auch telefonisch über unsere Geschäftsstelle.</div>

<div class="flat" style="left:203px"><div class="pic" role="img" aria-label="Foto: helles Mehrfamilienhaus unter blauem Himmel" style="background:linear-gradient(180deg,#8fb4dc,#e3d9b8 55%,#7f8f5a)"></div><b>Kelmsried (07491)</b>3-Raum | 58,04 m²<br>Ahornweg 35, 3. Obergeschoss<div class="btn">Zu den Details</div></div>
<div class="flat" style="left:452px"><div class="pic" role="img" aria-label="Foto: Wohnzimmer mit orangefarbenem Vorhang" style="background:linear-gradient(90deg,#e9dcc6,#e07a3a 30%,#f1e7d6 60%,#e6d8c2)"></div><b>Kelmsried (07491)</b>3-Raum | 58,04 m²<br>Ahornweg 35, 3. Obergeschoss<div class="btn">Zu den Details</div></div>
<div class="flat" style="left:700px"><div class="pic" role="img" aria-label="Foto: weißes Altbauhaus mit Bäumen" style="background:linear-gradient(90deg,#6b8a4a,#e8e6e0 35%,#d8d4cc 70%,#5d7a40)"></div><b>Kelmsried (07491)</b>3-Raum | 58,04 m²<br>Ahornweg 35, 3. Obergeschoss<div class="btn">Zu den Details</div></div>
<div class="flat" style="left:946px"><div class="pic" role="img" aria-label="Foto: rotes Backsteinhaus mit Balkonen" style="background:linear-gradient(180deg,#5a86c4,#b3603c 50%,#8a4a30)"></div><b>Kelmsried (07491)</b>3-Raum | 58,04 m²<br>Ahornweg 35, 3. Obergeschoss<div class="btn">Zu den Details</div></div>

<div class="abs kicker" style="left:206px;top:735px">Ihre Wohnungsbaugenossenschaft Kelmsried eG</div>
<div class="abs display welcome-title" style="left:205px;top:756px">Herzlich Willkommen</div>
<p class="abs body-text" style="left:206px;top:802px;width:680px">Informieren Sie sich über unsere Genossenschaft, das aktuelle Wohnungsangebot sowie über das umfangreiche Angebot an Dienstleistungen. Ob interessante Wohnungen, nach Ihren Wünschen gestaltet, ruhige Wohnlagen in 6 Gemeinden mit viel Grün, eine intakte Infrastruktur, vielseitigste Betreuungsleistungen oder auch gemeinsame Freizeitaktivitäten und Feste – wir bieten für jede Generation genau das Richtige und stehen Ihnen als kompetenter Partner gern zur Verfügung.</p>
<p class="abs body-text" style="left:206px;top:883px">Nehmen Sie mit uns Kontakt auf. Viel Spaß und eine gute Information wünscht Ihnen</p>
<div class="img" role="img" aria-label="Handschriftliche Unterschrift der Genossenschaft" style="left:202px;top:912px;width:256px;height:52px;background:linear-gradient(90deg,#f3f3f5,#ececf0)"></div>

<div class="abs kicker" style="left:201px;top:1002px">Das bieten wir Ihnen</div>
<div class="abs display welcome-title" style="left:201px;top:1024px">Dienstleistungen</div>
<div class="img" role="img" aria-label="Foto: Empfangstresen im Servicebüro" style="left:201px;top:1072px;width:211px;height:158px;background:linear-gradient(90deg,#9fb0c6,#d9dde4 40%,#3d9a8a 75%,#cfd6de)"></div>
<p class="abs body-text" style="left:431px;top:1071px;width:457px">Das Kompetenzzentrum organisiert, koordiniert und gestaltet das generationsübergreifende Wohnen in unserer Genossenschaft. Es umfasst alle Teilgebiete der Hilfe, Betreuung, Pflege, der Selbsthilfe, der Kommunikation und der Freizeitgestaltung einschließlich der Betreuung von Kindern.</p>
<p class="abs body-text" style="left:431px;top:1151px;width:457px">Die zentrale Anlaufstelle ist die Begegnungsstätte des Nachbarschaftsvereins, Ahornweg 13 in Kelmsried mit ihren Bereichen für Service und Dienstleistung sowie das Servicebüro der WBG Kelmsried eG. Beide Bereiche kommunizieren miteinander und sind territorial von allen Wohnungsstandorten der WBG Kelmsried eG auf kurzem Weg erreichbar</p>
<div class="btn" style="left:431px;top:1248px;width:168px;height:23px">Zu den Dienstleistungen</div>

<div class="abs kicker" style="left:203px;top:1312px">Bleiben Sie immer informiert</div>
<div class="abs display welcome-title" style="left:203px;top:1334px">News</div>

<div class="news" style="left:200px"><div class="pic" role="img" aria-label="Foto: Veranstaltung in einem Saal" style="background:linear-gradient(90deg,#8a5a40,#e7d9c8 40%,#c98a5c 80%,#7b4b35)"></div>
  <div class="card"><div class="date"><svg width="10" height="10" viewBox="0 0 10 10"><rect x=".5" y="1.5" width="9" height="8" fill="none" stroke="#888"/><rect x=".5" y="1.5" width="9" height="2" fill="#888"/></svg>26.07.2019</div><div class="ttl">Überschrift</div><div class="tx">Lorem ipsum dolor sit amet,<br>sadipscing elitr, sed diam...</div></div>
  <div class="btn">Mehr erfahren</div></div>
<div class="news" style="left:435px"><div class="pic" role="img" aria-label="Foto: Mieterfest im Freien" style="background:linear-gradient(180deg,#5e8a4c,#c7cfd6 45%,#6e8f55)"></div>
  <div class="card"><div class="date"><svg width="10" height="10" viewBox="0 0 10 10"><rect x=".5" y="1.5" width="9" height="8" fill="none" stroke="#888"/><rect x=".5" y="1.5" width="9" height="2" fill="#888"/></svg>25.03.2018</div><div class="ttl">Überschrift</div><div class="tx">Lorem ipsum dolor sit amet,<br>sadipscing elitr, sed diam...</div></div>
  <div class="btn">Mehr erfahren</div></div>
<div class="news" style="left:667px"><div class="pic" role="img" aria-label="Foto: Mieterfest im Freien" style="background:linear-gradient(180deg,#5e8a4c,#c7cfd6 45%,#6e8f55)"></div>
  <div class="card"><div class="date"><svg width="10" height="10" viewBox="0 0 10 10"><rect x=".5" y="1.5" width="9" height="8" fill="none" stroke="#888"/><rect x=".5" y="1.5" width="9" height="2" fill="#888"/></svg>25.03.2018</div><div class="ttl">Überschrift</div><div class="tx">Lorem ipsum dolor sit amet,<br>sadipscing elitr, sed diam...</div></div>
  <div class="btn">Mehr erfahren</div></div>

<div class="rbox" style="top:733px;height:137px;background:var(--box-dark);padding:14px 0 0 25px">
  <h3><svg width="18" height="18" viewBox="0 0 18 18"><circle cx="9" cy="5" r="4" fill="#fff"/><path d="M1 18c0-5 3.5-7 8-7s8 2 8 7z" fill="#fff"/></svg>KONTAKT</h3>
  <div class="row" style="margin-top:8px"><svg width="9" height="12" viewBox="0 0 10 14"><path d="M5 0C2.2 0 0 2.2 0 5c0 3.5 5 9 5 9s5-5.5 5-9c0-2.8-2.2-5-5-5zm0 7a2 2 0 110-4 2 2 0 010 4z" fill="#fff"/></svg>Lindenhofstraße 13, 07491 Kelmsried</div>
  <div class="row"><svg width="9" height="12" viewBox="0 0 10 17"><rect x="1" y="1" width="8" height="15" rx="1.5" fill="none" stroke="#fff" stroke-width="1.8"/></svg>03499 / 55 20 88</div>
  <div class="row"><svg width="11" height="10" viewBox="0 0 12 10"><rect x="1" y="3" width="10" height="7" fill="#fff"/><rect x="3" y="0" width="6" height="3" fill="#fff"/></svg>03499 / 55 14 530</div>
  <div class="row"><svg width="11" height="8" viewBox="0 0 12 9"><rect width="12" height="9" fill="#fff"/><path d="M0 0l6 5 6-5" stroke="var(--box-dark)" fill="none"/></svg>kontakt@wbg-kelmsried.example</div>
</div>
<div class="rbox" style="top:870px;height:140px;background:var(--box-mid);padding:14px 0 0 20px">
  <h3><svg width="20" height="20" viewBox="0 0 20 20"><circle cx="10" cy="10" r="8.5" fill="none" stroke="#fff" stroke-width="1.8"/><path d="M10 5v5l3 2" stroke="#fff" stroke-width="1.8" fill="none"/></svg>ÖFFNUNGSZEITEN</h3>
  <div class="hours" style="margin-top:6px">
    <b>Mo.:</b> 09.00 - 12.00 Uhr &amp; 13.00 - 16.00 Uhr<br>
    <b>Di.:</b> 09.00 - 12.00 Uhr &amp; 13.00 - 18.00 Uhr<br>
    <b>Mi.:</b> 10.00 - 12.00 Uhr &amp; 13.00 - 16.00 Uhr<br>
    <b>Do.:</b> 09.00 - 12.00 Uhr &amp; 13.00 - 15.30 Uhr<br>
    <b>Fr.:</b> 09.00 - 12.00 Uhr
  </div>
</div>
<div class="rbox" style="top:1010px;height:138px;background:var(--box-light);padding:12px 16px 0 20px">
  <h3><svg width="18" height="18" viewBox="0 0 18 18"><path d="M16 2a4 4 0 00-5 5L2 16l1 1 9-9a4 4 0 005-5l-2 2-2-1-1-2z" fill="#fff"/></svg>SERVICE / HAVARIE</h3>
  <div style="font-size:8.5px;line-height:11px;margin-top:8px;font-weight:400">Wir sind ständig bestrebt die Wohnqualität in unserer Genossenschaft zu steigern. Dazu gehört natürlich auch die Absicherung in Notsituationen. Unsere Havarienummer:</div>
  <div style="display:flex;align-items:center;gap:6px;font-family:'Baloo 2',sans-serif;font-size:19px;margin-top:4px;color:var(--blue);white-space:nowrap"><svg width="11" height="17" viewBox="0 0 10 17"><rect x="1" y="1" width="8" height="15" rx="1.5" fill="none" stroke="var(--blue)" stroke-width="1.8"/></svg>0176 / 5550 3170</div>
</div>
<div class="abs" style="left:935px;top:1148px;width:245px;height:614px;background:#f2f2f5"></div>
<div class="abs display" style="left:935px;width:245px;top:1163px;text-align:center;font-size:21px">Die Mieterzeitung</div>
<div class="abs" style="left:955px;width:205px;top:1195px;text-align:center;font-size:12.5px;line-height:16.5px;color:#777">Die 3.Ausgabe 2016 unserer Mieterzeitung steht zum Download bereit!</div>
<div class="img" role="img" aria-label="Titelseite der Mieterzeitung" style="left:1000px;top:1252px;width:123px;height:175px;background:linear-gradient(90deg,#8f9bd0 35%,#f4f1e2 35%)"></div>
<div class="btn" style="left:1013px;top:1437px;width:97px;height:23px">Zum Archive</div>
<div class="abs display" style="left:935px;width:245px;text-align:center;top:1482px;font-size:19px">Wohnungsstandorte</div>
<div class="loc alt" style="top:1520px">Kelmsried (07491)</div>
<div class="loc" style="top:1544px">Erlenau, OT Birkhain (07493)</div>
<div class="loc alt" style="top:1568px">Hainsdorf (07495)</div>
<div class="loc" style="top:1592px">Moosbach (07497)</div>
<div class="loc alt" style="top:1616px">Tannrode (07498)</div>
<div class="loc" style="top:1640px">Weidenthal (07499)</div>
<div class="btn" style="left:994px;top:1671px;width:141px;height:24px">Zur Wohnungssuche</div>

<div class="abs contact-sec"></div>
<div class="abs kicker" style="left:185px;width:1015px;text-align:center;top:1845px">Nehmen Sie Kontakt zu uns auf</div>
<div class="abs display" style="left:185px;width:1015px;text-align:center;top:1868px;font-size:30px">Kontakt</div>
<div class="img" role="img" aria-label="Foto: Gruppe jubelnder junger Menschen mit erhobenem Daumen" style="left:190px;top:1905px;width:330px;height:305px;background:radial-gradient(ellipse at 50% 55%,#c9b9a8 0%,#9aa6c8 45%,rgba(241,241,246,0) 72%)"></div>
<div class="abs" style="left:546px;top:1968px;display:flex;align-items:center;gap:10px;font-family:'Comfortaa',sans-serif;font-weight:700;font-size:26px;color:var(--blue)"><span style="width:16px;height:16px;background:var(--red)"></span>wbg Kelmsried</div>
<div class="abs caddr" style="left:546px;top:2046px"><svg width="12" height="16" viewBox="0 0 10 14"><path d="M5 0C2.2 0 0 2.2 0 5c0 3.5 5 9 5 9s5-5.5 5-9c0-2.8-2.2-5-5-5zm0 7a2 2 0 110-4 2 2 0 010 4z" fill="var(--blue)"/></svg>Lindenhofstraße 13, 07491 Kelmsried</div>
<div class="abs caddr" style="left:546px;top:2075px"><svg width="12" height="17" viewBox="0 0 10 17"><rect x="1" y="1" width="8" height="15" rx="1.5" fill="none" stroke="var(--blue)" stroke-width="1.8"/></svg>03499 / 55 20 88</div>
<div class="abs caddr" style="left:546px;top:2104px"><svg width="14" height="12" viewBox="0 0 12 10"><rect x="1" y="3" width="10" height="7" fill="var(--blue)"/><rect x="3" y="0" width="6" height="3" fill="var(--blue)"/></svg>03499 / 55 14 530</div>

<div class="abs field-label" style="left:803px;top:1933px"><svg width="10" height="10" viewBox="0 0 18 18"><circle cx="9" cy="5" r="4" fill="#666"/><path d="M1 18c0-5 3.5-7 8-7s8 2 8 7z" fill="#666"/></svg>Ihr Vorname / Nachname*</div>
<div class="field" style="top:1955px"></div>
<div class="abs field-label" style="left:803px;top:2002px"><svg width="10" height="10" viewBox="0 0 18 18"><circle cx="9" cy="5" r="4" fill="#666"/><path d="M1 18c0-5 3.5-7 8-7s8 2 8 7z" fill="#666"/></svg>Ihre Nachricht*</div>
<div class="field" style="top:2025px"></div>
<div class="abs" style="left:803px;top:2078px;width:210px;font-size:10px;line-height:12px;color:#777">Die mit * gekennzeichneten Felder sind Pflichtfelder. Ihre Daten werden vertraulich behandelt.</div>
<div class="btn" style="left:1075px;top:2078px;width:96px;height:23px">Ab die Post</div>

<svg class="abs" style="left:185px;top:2150px" width="1015" height="358" viewBox="0 0 1015 358" preserveAspectRatio="none"><path d="M0 65C300 45 700 50 1015 0V358H0z" fill="var(--lav)"/></svg>
<div class="abs" style="left:204px;top:2262px;display:flex;align-items:center;gap:8px;font-family:'Comfortaa',sans-serif;font-weight:700;font-size:20px;color:var(--blue)"><span style="width:12px;height:12px;background:var(--red)"></span>wbg Kelmsried</div>
<div class="abs caddr" style="left:204px;top:2328px;color:#fff;font-size:12.5px"><svg width="12" height="16" viewBox="0 0 10 14"><path d="M5 0C2.2 0 0 2.2 0 5c0 3.5 5 9 5 9s5-5.5 5-9c0-2.8-2.2-5-5-5zm0 7a2 2 0 110-4 2 2 0 010 4z" fill="#fff"/></svg>Lindenhofstraße 13, 07491 Kelmsried</div>
<div class="abs caddr" style="left:204px;top:2357px;color:#fff;font-size:12.5px"><svg width="12" height="17" viewBox="0 0 10 17"><rect x="1" y="1" width="8" height="15" rx="1.5" fill="none" stroke="#fff" stroke-width="1.8"/></svg>03499 / 55 20 88</div>
<div class="abs caddr" style="left:204px;top:2386px;color:#fff;font-size:12.5px"><svg width="14" height="12" viewBox="0 0 12 10"><rect x="1" y="3" width="10" height="7" fill="#fff"/><rect x="3" y="0" width="6" height="3" fill="#fff"/></svg>03499 / 55 14 530</div>

<div class="abs foot-head" style="left:481px;top:2244px">ÖFFNUNGSZEITEN</div>
<div class="abs foot-text fhours" style="left:483px;top:2283px">
  <b>Mo.:</b> 09.00 - 12.00 Uhr &amp; 13.00 - 16.00 Uhr<br>
  <b>Di.:</b> 09.00 - 12.00 Uhr &amp; 13.00 - 18.00 Uhr<br>
  <b>Mi.:</b> 10.00 - 12.00 Uhr &amp; 13.00 - 16.00 Uhr<br>
  <b>Do.:</b> 09.00 - 12.00 Uhr &amp; 13.00 - 15.30 Uhr<br>
  <b>Fr.:</b> 09.00 - 12.00 Uhr
</div>
<div class="abs foot-head" style="left:742px;top:2244px">NAVIGATION</div>
<div class="abs fnav" style="left:745px;top:2283px">Home<br>Die Genossenschaft<br>Wohnungssuche<br>Aktuelles<br>Havariedienst<br>Kontakt<br>Datenschutzerklärung</div>
<div class="abs foot-head" style="left:937px;top:2244px">UMFRAGE</div>
<div class="abs foot-text" style="left:937px;top:2285px;width:236px;height:143px;background:#58585c;padding:8px 10px;font-size:11.5px;line-height:17px">DIE WOHNUNG DER ZUKUNFT ...<br>... Eine mitalternde Wohnung ...<br><br>Beteiligen Sie sich mit Vorschlägen. Ihre Meinungen und Vorschläge sind uns wichtig!</div>

<div class="abs" style="left:204px;top:2433px;width:966px;height:1px;background:#fff"></div>
<div class="abs" style="left:185px;width:1015px;top:2452px;text-align:center;color:#fff;font-size:13.5px;font-weight:400">© Unternehmensname 2019. All rights reserved.</div>
<div class="abs" style="left:185px;width:1015px;top:2474px;text-align:center;color:#fff;font-family:'Oswald',sans-serif;font-size:9.5px;font-weight:300">SERVICE &nbsp;|&nbsp; MIETERZEITUNG &nbsp;|&nbsp; PARTNER &nbsp;|&nbsp; DOWNLOAD &nbsp;|&nbsp; IMPRESSUM &nbsp;|&nbsp; DATENSCHUTZERKLÄRUNG</div>

</body>
</html>
```